Label or packaging Design for Hair Care Line

Dear Designer,
We are Corvella, a brand known for our premium hairstyling tools, and we are excited to expand into hair care. We are currently looking for a talented designer to create the label designs for our entire luxury hair care line.
This project is crucial in establishing our visual identity in the hair care market, and we aim to position ourselves alongside premium brands such as LTP, Dorvane Hair Atelier, and Pelmi.
Project Scope
We need a cohesive label design for our hair care line, which includes:
5 products (e.g., shampoo, conditioner, hair oil, styling cream, and a hair mask).
The designs should include:
Front label: Highlighting the product name, key features, and branding.
Our goal is to achieve a design that communicates premium luxury with a touch of professionalism. Below are the specific guidelines to help you align with our vision:
Style and Inspiration
Think of brands like LTP, Dorvane Hair Atelier, and Pelmi.
Luxury and Minimalism: Clean lines, sophisticated typography, and an elegant color palette.
Subtle femininity: premium finishes like metallic accents (gold, silver, or rose gold).
Brand Personality
Premium: Reflecting high quality and exclusivity.
Modern & Professional: Appealing to a refined, professional audience but also suitable for lifestyle-oriented customers.
Warm & Empowering: A brand that celebrates confidence and individuality.
Color Palette
Neutral tones like black, white, accented with metallics (gold or silver) for a luxurious feel.
Colors that feel timeless and elegant rather than trendy or overly bright.
Typography
Use clean, modern fonts (preferably sans-serif or serif for a refined look).
Clear and legible for all product details while maintaining a high-end aesthetic.
Materials and Finishes
Packaging Shape
The label designs should suit a variety of bottle and jar shapes (e.g., cylindrical, flat, or rounded).
Keep scalability in mind so the identity remains consistent across different products.
Deliverables
To understand the aesthetic we are aiming for, here are some brands to use as inspiration:
LTP: For its minimalistic and modern approach.
Dorvane Hair Atelier: For its combination of luxury and professional appeal.
Pelmi: For its soft femininity and lifestyle branding.
we would like to see your designs applied to a variety of packaging types to get an overall impression of how the brand identity works across different product formats. This includes:
A squeeze bottle (e.g., for styling creams or conditioners).
A glass bottle with a dropper (e.g., for a luxurious hair oil).
A shampoo/conditioner bottle (standard pump or flip-top cap).
A spray bottle (e.g., for leave-in treatments or heat protectors).
By creating designs for these different packaging types, we can better evaluate how cohesive and versatile the brand identity will be across the entire product line.

Updates
As you may have noticed from the designs, they don’t quite align with our briefing. The look needs to be clean and professional, similar to Dorvane, LTP, and the other examples we provided. Please address this, and we’ll check it!

Target Market(s)
europe and us
Font styles to use
Other font styles liked:
- century gothic

Look and feel
Each slider illustrates characteristics of the customer's brand and the style your logo design should communicate.

```html
<!DOCTYPE html>
<html lang="en">
<head>
<meta charset="utf-8">
<title>Corvella — Hair Care Label System</title>
<link rel="stylesheet" href="https://fonts.googleapis.com/css2?family=Questrial&display=swap">
<style>
  :root {
    --backdrop: #e9ebee;
    --label-white: #ffffff;
    --label-edge: #d9dcdf;
    --ink: #3a3b3d;
    --ink-soft: #555658;
    --band: #505153;
    --band-text: #f4f4f4;
    --gold-light: #e6cf94;
    --gold: #c49a45;
    --gold-deep: #a67c2c;
  }
  * { box-sizing: border-box; margin: 0; padding: 0; }
  html, body { width: 1200px; height: 721px; overflow: hidden; }
  body {
    background: var(--backdrop);
    font-family: "Questrial", "Century Gothic", sans-serif;
    color: var(--ink);
    position: relative;
  }
  .label-line {
    position: absolute; inset: 0;
    display: flex; align-items: center; justify-content: center; gap: 46px;
  }
  .label {
    position: relative;
    display: flex;
    flex-direction: column;
    background: var(--label-white);
    border: 1px solid var(--label-edge);
    box-shadow: 0 6px 22px rgba(40, 48, 60, 0.10);
  }
  .brand {
    font-weight: 400;
    letter-spacing: 0.5px;
    color: var(--ink);
    line-height: 1;
  }
  .label-body {
    margin-top: auto;
    display: flex;
    flex-direction: column;
  }
  .tagline {
    position: absolute;
    background: var(--band);
    color: var(--band-text);
    writing-mode: vertical-rl;
    letter-spacing: 0.8px;
    display: flex; align-items: center; justify-content: center;
    white-space: nowrap;
  }
  .gold-rule {
    height: 1.5px;
    flex: none;
    background: linear-gradient(90deg, var(--gold-deep), var(--gold-light) 45%, var(--gold) 75%, var(--gold-deep));
  }
  .product-name {
    font-weight: 400;
    text-transform: uppercase;
    line-height: 1.12;
    letter-spacing: 0.6px;
    color: var(--ink);
  }
  .description {
    text-align: justify;
    color: var(--ink-soft);
    line-height: 1.45;
  }
  .volume {
    align-self: flex-end;
    color: var(--ink-soft);
    letter-spacing: 0.3px;
    line-height: 1;
    white-space: nowrap;
  }

  /* Sculpting hair cream — squeeze bottle */
  .label--cream { width: 220px; height: 470px; padding: 40px 22px 28px; }
  .label--cream .brand { font-size: 30px; }
  .label--cream .tagline { top: 0; right: 24px; width: 16px; height: 150px; font-size: 8px; }
  .label--cream .rule-top, .label--cream .rule-mid { width: 150px; }
  .label--cream .product-name { font-size: 21px; margin: 10px 0; }
  .label--cream .description { width: 165px; font-size: 7.6px; margin-top: 12px; }
  .label--cream .volume { font-size: 8px; margin: 10px 0 8px; }
  .label--cream .rule-base { width: 176px; }

  /* Luxe hair oil — dropper bottle */
  .label--oil { width: 150px; height: 200px; padding: 18px 14px 10px; }
  .label--oil .brand { font-size: 17px; }
  .label--oil .tagline { top: 0; right: 8px; width: 11px; height: 130px; font-size: 5px; }
  .label--oil .rule-top, .label--oil .rule-mid { width: 40px; }
  .label--oil .product-name { font-size: 12px; margin: 6px 0; }
  .label--oil .description { width: 104px; font-size: 4.6px; margin-top: 7px; }
  .label--oil .volume { font-size: 5px; margin: 6px 0 5px; }
  .label--oil .rule-base { width: 118px; }

  /* Restorative conditioner — flip-top bottle */
  .label--conditioner { width: 300px; height: 500px; padding: 48px 28px 28px; }
  .label--conditioner .brand { font-size: 40px; }
  .label--conditioner .tagline { top: 40px; right: 14px; width: 22px; height: 240px; font-size: 10px; }
  .label--conditioner .rule-top, .label--conditioner .rule-mid { width: 228px; }
  .label--conditioner .product-name { font-size: 25px; margin: 12px 0; }
  .label--conditioner .description { width: 228px; font-size: 8.9px; margin-top: 14px; }
  .label--conditioner .volume { font-size: 11px; margin: 12px 0 8px; }
  .label--conditioner .rule-base { width: 244px; }

  /* Thermal shield spray — mist bottle */
  .label--spray { width: 180px; height: 360px; padding: 30px 18px 14px; }
  .label--spray .brand { font-size: 22px; }
  .label--spray .tagline { top: 0; right: 14px; width: 12px; height: 135px; font-size: 5.5px; }
  .label--spray .rule-top, .label--spray .rule-mid { width: 84px; }
  .label--spray .product-name { font-size: 14px; margin: 8px 0; }
  .label--spray .description { width: 136px; font-size: 5.2px; margin-top: 8px; }
  .label--spray .volume { font-size: 5.5px; margin: 8px 0 6px; }
  .label--spray .rule-base { width: 144px; }
</style>
</head>
<body>
<main class="label-line">

  <article class="label label--cream">
    <div class="brand">corvella</div>
    <div class="tagline">Smooth. Define. Empower.</div>
    <div class="label-body">
      <div class="gold-rule rule-top"></div>
      <h2 class="product-name">Sculpting<br>Hair<br>Cream</h2>
      <div class="gold-rule rule-mid"></div>
      <p class="description">Elevate your styling routine with our premium sculpting hair cream. This multifunctional cream is designed to add definition, smoothness, and control to your hair while nourishing it from root to tip. Formulated with high-quality ingredients, it tames frizz, enhances shine, and provides long-lasting hold without feeling heavy or sticky. Whether you want a polished, sleek look or soft, natural waves, this cream is your go-to solution for effortless styling.</p>
      <div class="volume">200 ml / 6.8 fl oz</div>
      <div class="gold-rule rule-base"></div>
    </div>
  </article>

  <article class="label label--oil">
    <div class="brand">corvella</div>
    <div class="tagline">Smooth. Define. Empower.</div>
    <div class="label-body">
      <div class="gold-rule rule-top"></div>
      <h2 class="product-name">Luxe<br>Hair<br>Oil</h2>
      <div class="gold-rule rule-mid"></div>
      <p class="description">A premium hair oil designed to provide deep moisture, instant shine and protection against damage.</p>
      <div class="volume">50 ml / 1.7 fl oz</div>
      <div class="gold-rule rule-base"></div>
    </div>
  </article>

  <article class="label label--conditioner">
    <div class="brand">corvella</div>
    <div class="tagline">Cleanse. Nourish. Rejuvenate.</div>
    <div class="label-body">
      <div class="gold-rule rule-top"></div>
      <h2 class="product-name">Restorative<br>Conditioner</h2>
      <div class="gold-rule rule-mid"></div>
      <p class="description">Indulge your hair with our hydrating shampoo, a luxurious formula that gently cleanses while delivering intense moisture and nourishment. Enriched with premium botanical ingredients, it restores balance to your scalp and hair, leaving it soft, smooth, and manageable. Perfect for daily use and suitable for all hair types, it helps to maintain healthy, vibrant locks.</p>
      <div class="volume">300 ml / 10.1 fl oz</div>
      <div class="gold-rule rule-base"></div>
    </div>
  </article>

  <article class="label label--spray">
    <div class="brand">corvella</div>
    <div class="tagline">Protect. Strengthen. Style.</div>
    <div class="label-body">
      <div class="gold-rule rule-top"></div>
      <h2 class="product-name">Thermal<br>Shield<br>Spray</h2>
      <div class="gold-rule rule-mid"></div>
      <p class="description">Shield your hair from heat damage with our thermal shield spray, an essential styling treatment for all hair types. Formulated with advanced heat-activated protection, it creates a protective barrier to resist breakage and prevent damage from styling tools up to 230°C. Enriched with strengthening proteins and hydrating extracts, it enhances shine, reduces frizz, and leaves your hair smooth and silky.</p>
      <div class="volume">200 ml / 6.8 fl oz</div>
      <div class="gold-rule rule-base"></div>
    </div>
  </article>

</main>
</body>
</html>
```